UPDATED BRIEF: Hypermobile EDS Book Cover Contest

I am writing a print book. I need cover designs to evaluate with your creativity. It is a nonfiction memoir meets self-help guide to living with a rare, incurable chronic illness called EDS. See attached Word doc for book details and copy. It is designed to be an inspiration story of living well with this disease so mindset is a key theme. I'm looking for all types of ideas including photography (sailboat, mountain, journey concepts), type flat designs highlighting hypermobility (a key part of the disease), including good use of color and white space. I want it to be legible, intriguing, and emotive if possible. I need someone to be able to produce and provide the production files and/or edit the final text back copy as it is not yet final. I will be sharing the contest with my fan base. I will ultimately need the cover, back cover, spine, and audio and ebook covers done all the same just reformatted to size. Print book 6x9 to be done first. I dont want to provide too much direction so you can be creative.
Updates

I uploaded a new brief for updated author name and back cover. Please update and I will start the poll. I will also extend the project timeline.

Can anyone create a design with the typeset words of hypermobile on the title being "pinched" by a string? Like holding it all together by a string?

Went on vacation/holiday

Target Market(s)

chronic illness disease victims, specifically those with Hypermobile Ehlers Danlos Syndrome (EDS), dysautonomia (POTS) or craniocervical instability in the neck

Industry/Entity Type

Self help, personal development, memoir

Font styles to use
Sans Serif

Colors
FFC000
F8CF3A
FAE287
FDF2CF
FEFAEE

Requirements
Must have
• legible, intriguing even emotive design with text or photos
Nice to have
• Potentially visually showing a journey, hypermobility, or overcoming obstacles
Should not have
• black dark backgrounds

```html
<!DOCTYPE html>
<html lang="en">
<head>
<meta charset="UTF-8">
<title>Keeping It All Steady When You're Hypermobile: Book Cover</title>
<link href="https://fonts.googleapis.com/css2?family=Montserrat:wght@400;500&display=swap" rel="stylesheet">
<style>
  :root {
    --paper: #fdfdfd;
    --ink: #1b1b1b;
    --accent: #d9191f;
    --mist: #ececec;
    --rock-mid: #8a8a8a;
    --rock-dark: #2a2a2a;
    --author: #ffffff;
  }
  html, body {
    margin: 0;
    padding: 0;
    width: 800px;
    height: 1200px;
    overflow: hidden;
    background: var(--paper);
  }
  .cover {
    position: relative;
    width: 800px;
    height: 1200px;
    background: var(--paper);
    font-family: "Montserrat", sans-serif;
    color: var(--ink);
    overflow: hidden;
  }
  .cover__photo {
    position: absolute;
    left: 0;
    right: 0;
    top: 690px;
    bottom: 0;
    background:
      linear-gradient(105deg, rgba(253,253,253,0) 40%, rgba(240,240,240,0.9) 72%, rgba(253,253,253,0.3) 100%),
      linear-gradient(to bottom, var(--paper) 0%, var(--mist) 15%, var(--rock-mid) 42%, var(--rock-dark) 78%, #1e1e1e 100%);
  }
  .cover__tagline {
    position: absolute;
    top: 42px;
    left: 0;
    width: 100%;
    margin: 0;
    text-align: center;
    font-size: 19px;
    font-weight: 500;
    letter-spacing: 0.14em;
    text-indent: 0.14em;
    line-height: 26px;
    text-transform: uppercase;
  }
  .cover__title {
    position: absolute;
    top: 0;
    left: 0;
    width: 100%;
    margin: 0;
    font-weight: 500;
    font-size: 51px;
    text-transform: uppercase;
  }
  .cover__title-line {
    position: absolute;
    left: 0;
    width: 100%;
    text-align: center;
    letter-spacing: 0.27em;
    text-indent: 0.27em;
    line-height: 1;
  }
  .cover__title-line--1 { top: 154px; }
  .cover__title-line--2 { top: 270px; }
  .cover__title-line--3 { top: 386px; }
  .cover__title-line--4 { top: 501px; letter-spacing: 0.25em; text-indent: 0.25em; }
  .cover__title-line--5 { top: 617px; color: var(--accent); letter-spacing: 0.22em; text-indent: 0.22em; }
  .cover__author {
    position: absolute;
    top: 597px;
    left: 0;
    width: 100%;
    margin: 0;
    transform: translateY(500px);
    text-align: center;
    font-size: 50px;
    font-weight: 500;
    line-height: 1;
    letter-spacing: 0.17em;
    text-indent: 0.17em;
    color: var(--author);
    text-transform: uppercase;
  }
</style>
</head>
<body>
  <main class="cover">
    <div class="cover__photo" role="img" aria-label="Black and white photograph of a forested mountain peak wrapped in drifting white clouds"></div>
    <p class="cover__tagline">Achieve a better life experience<br>with EDS, POTS, and instability</p>
    <h1 class="cover__title">
      <span class="cover__title-line cover__title-line--1">Keeping</span>
      <span class="cover__title-line cover__title-line--2">It All</span>
      <span class="cover__title-line cover__title-line--3">Steady</span>
      <span class="cover__title-line cover__title-line--4">When You’re</span>
      <span class="cover__title-line cover__title-line--5">Hypermobile</span>
    </h1>
    <p class="cover__author">Marnie H. Cole</p>
  </main>
</body>
</html>
```